Prepared Meal Delivery Website

Need a new modern design for a prepared meal delivery company that is hosted on Shopify.

Target Market(s)

Young Professionals

Industry/Entity Type

Prepared Meal Delivery Service

Number of Pages Required

5+ page

Requirements
Must have
• Use https://www.velmorafoods.com/ as an example
Nice to have
• Vibrant page with call to action obvious and repeated
Should not have
• Generic look, grays/white/black

```html
<!DOCTYPE html>
<html lang="en">
<head>
<meta charset="utf-8">
<title>Go Fuel Meals — Prepared Meal Delivery</title>
<link href="https://fonts.googleapis.com/css2?family=Montserrat:ital,wght@0,400;0,500;0,600;0,700;1,400&display=swap" rel="stylesheet">
<style>
:root{
  --orange:#f25c19;
  --orange-dark:#e04f10;
  --navy:#2c3b4b;
  --navy-deep:#263445;
  --ink:#2b2b2b;
  --muted:#666;
  --card:#f3f3f6;
  --line:#cfcfcf;
  --white:#fff;
}
*{box-sizing:border-box;margin:0;padding:0}
html,body{width:1200px;height:4501px;overflow:hidden}
body{font-family:'Montserrat',sans-serif;color:var(--ink);background:var(--white);position:relative}
section,header,footer,.topbar{position:relative;width:1200px;overflow:hidden}
.abs{position:absolute}
.accent{color:var(--orange)}
.btn{display:inline-flex;align-items:center;justify-content:center;height:30px;padding:0 22px;border-radius:16px;font-size:11px;font-weight:700;text-decoration:none;white-space:nowrap}
.btn-solid{background:var(--orange);color:#fff}
.btn-outline{border:2px solid var(--ink);color:var(--ink);background:#fff}
.btn-light{border:2px solid #fff;color:#fff}
.section-title{position:absolute;left:0;width:1200px;text-align:center;font-size:23px;font-weight:700;color:#222}

/* top bar */
.topbar{height:24px;background:var(--orange);color:#fff;font-size:9.5px;white-space:nowrap}
.topbar .notice{position:absolute;left:358px;top:6px}
.topbar .contact{position:absolute;left:850px;top:6px;display:flex;gap:16px;font-weight:500}

/* header */
.site-header{height:69px;background:#fff;border-bottom:1px solid #eee;overflow:visible;z-index:2}
.brand{position:absolute;left:92px;top:-20px;width:88px;height:88px;border-radius:50%;background:var(--orange);display:flex;align-items:center;justify-content:center;color:#fff;font-size:11px;font-weight:700;text-align:center;line-height:1.3;padding:0 12px}
.nav{position:absolute;left:268px;top:29px;display:flex;gap:22px;font-size:9.5px;font-weight:600;color:#333;white-space:nowrap}
.nav .active{color:var(--orange)}
.header-tools{position:absolute;left:943px;top:20px;display:flex;gap:8px;align-items:center}
.tool{width:30px;height:30px;border:1.5px solid #333;border-radius:50%;display:flex;align-items:center;justify-content:center}
.cart{margin-left:12px;width:86px;height:32px;border-radius:16px;background:var(--orange);color:#fff;font-size:10px;font-weight:700;display:flex;align-items:center;justify-content:center;gap:6px}

/* hero */
.hero{height:375px;background:linear-gradient(90deg,#eef0ec 0%,#e3e6df 45%,#d8dccf 100%)}
.hero h1{position:absolute;left:200px;top:92px;font-size:31px;line-height:1.25;font-weight:700;color:#222}
.hero p{position:absolute;left:200px;top:178px;font-size:14px;width:340px;color:#444}
.hero .btn{position:absolute;left:200px;top:244px}
.hero-plate{position:absolute;left:625px;top:-30px;width:480px;height:480px;border-radius:50%;background:radial-gradient(circle,#f4efe4 0%,#e8d9bb 45%,#9a7a55 70%,#f7f7f5 72%);border:2px solid #444}

/* how it works */
.how{height:486px}
.how .section-title{top:62px}
.step{position:absolute;top:170px;width:250px;height:190px;border:1px solid #999;text-align:center;padding:52px 18px 0}
.step h3{font-size:15px;font-weight:600;margin-bottom:14px}
.step p{font-size:11px;line-height:1.7;color:#555}
.step-icon{position:absolute;left:78px;top:-56px;width:94px;height:94px;border-radius:50%;background:#fff;border:1px solid #999;display:flex;align-items:center;justify-content:center}
.how .btn{position:absolute;left:532px;top:407px;width:136px}

/* shop */
.shop{height:630px;background:linear-gradient(180deg,#3d4c5e 0%,#324255 60%,#2c3b4b 100%)}
.shop .kicker{position:absolute;top:60px;width:1200px;text-align:center;color:#fff;font-size:14px}
.shop h2{position:absolute;top:84px;width:1200px;text-align:center;color:#fff;font-size:23px;font-weight:700}
.cat{position:absolute;width:182px;height:170px;background:#fff}
.cat .shot{position:absolute;left:36px;top:14px;width:110px;height:110px;border-radius:50%}
.cat span{position:absolute;bottom:10px;width:100%;text-align:center;font-size:12px;font-weight:600;color:#333}
.cat.on span{background:var(--orange);color:#fff;bottom:0;height:34px;line-height:34px}
.shop .btn{position:absolute;left:537px;top:536px;width:126px}

/* who */
.who{height:481px}
.who .section-title{top:58px}
.persona{position:absolute;top:111px;width:240px;text-align:center}
.persona .shot{width:124px;height:124px;border-radius:50%;margin:0 auto 16px}
.persona h3{font-size:15px;font-weight:600;margin-bottom:14px}
.persona p{font-size:10px;line-height:1.55;color:#555}
.who .btn{position:absolute;left:532px;top:388px;width:136px}

/* team */
.team{height:366px;background:var(--orange);color:#fff}
.team h2{position:absolute;left:200px;top:96px;font-size:21px;line-height:1.3;font-weight:700}
.team .btn{position:absolute;left:200px;top:172px;width:114px}
.member{position:absolute;top:62px;width:182px;text-align:center}
.member .shot{width:182px;height:180px;margin-bottom:20px}
.member h3{font-size:14px;font-weight:600}
.member p{font-size:11px;margin-top:6px}

/* bag */
.bag{height:552px}
.bag .section-title{top:56px}
.feature{position:absolute;top:145px;width:182px;height:282px;background:var(--card);padding:62px 12px 0 12px}
.feature .ficon{position:absolute;left:12px;top:-40px;width:74px;height:74px;border-radius:50%;background:#fff;border:1.5px solid #555;display:flex;align-items:center;justify-content:center}
.feature h3{font-size:12px;font-weight:600;line-height:1.3;margin-bottom:14px}
.feature p{font-size:9px;line-height:1.7;color:#666}
.bag .btn{position:absolute;left:518px;top:460px;width:164px}

/* gift */
.gift{height:313px;background:var(--navy)}
.gift h2{position:absolute;left:93px;top:58px;font-size:29px;font-weight:700;color:#fff}
.gift p{position:absolute;left:93px;top:112px;width:420px;font-size:13px;line-height:1.7;color:#fff}
.gift .btn{position:absolute;left:93px;top:220px;width:162px}
.gift-photo{position:absolute;left:538px;top:32px;width:630px;height:250px;background:linear-gradient(120deg,#b9b1a4 0%,#e9e6df 55%,#d4d0c4 100%)}

/* testimonials */
.reviews{height:430px}
.reviews .section-title{top:62px}
.quote-badge{position:absolute;left:564px;top:114px;width:72px;height:72px;border-radius:50%;border:2px solid var(--orange);display:flex;align-items:center;justify-content:center}
.quote-badge div{width:54px;height:54px;border-radius:50%;background:var(--orange);display:flex;align-items:center;justify-content:center;color:#fff;font-size:30px;font-weight:700}
.reviews blockquote{position:absolute;left:280px;top:198px;width:640px;text-align:center;font-style:italic;font-size:12px;line-height:1.6;color:#444}
.reviews .by{position:absolute;top:327px;width:1200px;text-align:center;color:var(--orange);font-size:13px;font-weight:600}
.dots{position:absolute;top:356px;left:562px;display:flex;gap:12px}
.dots i{width:10px;height:10px;border-radius:50%;border:1.5px solid #444}
.dots i.on{background:#444;box-shadow:inset 0 0 0 2px #fff}
.arrow{position:absolute;top:268px}

/* join */
.join{height:312px;background:linear-gradient(90deg,#f6f6f6 0%,#f1efec 45%,#e9e4dc 60%)}
.join-photo{position:absolute;left:700px;top:0;width:500px;height:312px;background:linear-gradient(135deg,#e4a36a 0%,#c1502a 45%,#7b8f3e 75%,#b4652e 100%)}
.join h2{position:absolute;left:93px;top:82px;font-size:29px;font-weight:700;color:#222}
.join p{position:absolute;left:93px;top:140px;width:480px;font-size:14px;line-height:1.55;color:#444}
.join .b1{position:absolute;left:93px;top:212px;width:120px}
.join .b2{position:absolute;left:219px;top:212px;width:120px}

/* footer */
.site-footer{height:463px;background:var(--navy-deep);color:#fff}
.footer-brand{position:absolute;left:93px;top:44px;width:156px;height:156px;border-radius:50%;border:2px solid #fff;display:flex;align-items:center;justify-content:center;text-align:center;font-size:16px;font-weight:600;line-height:1.3;padding:0 24px}
.fcol{position:absolute;top:62px}
.fcol h4{font-size:13px;font-weight:600;margin-bottom:16px;white-space:nowrap}
.fcol li{list-style:none;font-size:9.5px;line-height:1.55}
.fcol .row{display:flex;align-items:center;gap:8px;font-size:11px;margin-bottom:12px;white-space:nowrap}
.socials{display:flex;gap:10px;margin-top:18px}
.socials i{width:28px;height:28px;border-radius:50%;background:#fff;display:block}
.socials i.on{background:var(--orange)}
.newsletter p{font-size:9.5px;line-height:1.5;width:240px;margin-bottom:10px}
.newsletter .field{width:238px;height:28px;border-radius:14px;background:#fff;color:#333;font-size:9.5px;padding:8px 16px}
.newsletter .btn{margin-top:10px;width:94px;height:30px}
.footer-rule{position:absolute;left:200px;top:243px;width:800px;height:1px;background:#5a6777}
.cities h5{position:absolute;left:200px;top:266px;font-size:10px;font-weight:600}
.cities p{position:absolute;left:200px;top:296px;width:800px;font-size:9.5px;line-height:1.95}
.copy{position:absolute;top:420px;width:1200px;text-align:center;font-size:9.5px}
</style>
</head>
<body>

<div class="topbar">
  <div class="notice">Orders Placed Now Will Be Delivered On <b>Sunday Aug 7th</b> And <b>Wednesday Aug 10th.</b></div>
  <div class="contact"><span>✉ hello@gofuelmeals.com</span><span>☏ (416) 555 0142</span></div>
</div>

<header class="site-header">
  <div class="brand">Go Fuel Meals</div>
  <nav class="nav">
    <span class="active">HOME</span><span>SHOP NOW</span><span>SUBSCRIPTIONS</span><span>BUSINESS PLAN</span><span>GIFT CARDS</span><span>REWARDS</span><span>ABOUT US</span><span>CONTACT US</span>
  </nav>
  <div class="header-tools">
    <div class="tool"><svg width="12" height="12" viewBox="0 0 12 12"><circle cx="5" cy="5" r="3.5" fill="none" stroke="#333" stroke-width="1.5"/><line x1="7.5" y1="7.5" x2="11" y2="11" stroke="#333" stroke-width="1.5"/></svg></div>
    <div class="tool"><svg width="12" height="12" viewBox="0 0 12 12"><circle cx="6" cy="4" r="2.5" fill="#333"/><path d="M1.5 11.5c0-3 2-4.5 4.5-4.5s4.5 1.5 4.5 4.5z" fill="#333"/></svg></div>
    <div class="cart"><svg width="12" height="11" viewBox="0 0 12 11"><path d="M0 1h2l2 6h6l1.5-4.5H3" fill="none" stroke="#fff" stroke-width="1.5"/><circle cx="5" cy="9.5" r="1" fill="#fff"/><circle cx="9" cy="9.5" r="1" fill="#fff"/></svg>$0.00</div>
  </div>
</header>

<section class="hero">
  <h1>Everything You Need<br>to Know</h1>
  <p><span class="accent">Go Fuel Meals</span> is not just a food delivery service, it's a community.</p>
  <a class="btn btn-solid">Start Your Journey</a>
  <div class="hero-plate" role="img" aria-label="Plate of glazed chicken with noodles, broccoli and carrots"></div>
</section>

<section class="how">
  <h2 class="section-title">How the <span class="accent">GFM</span> lifestyle plan works</h2>
  <div class="step" style="left:199px">
    <div class="step-icon"><svg width="44" height="44" viewBox="0 0 44 44" fill="none" stroke="#f25c19" stroke-width="1.6"><rect x="10" y="6" width="24" height="32" rx="2"/><line x1="15" y1="16" x2="29" y2="16"/><line x1="15" y1="22" x2="29" y2="22"/><line x1="15" y1="28" x2="25" y2="28"/></svg></div>
    <h3>Choose a plan</h3>
    <p>Choose one of our pre-set plans<br>or Build Your Own!</p>
  </div>
  <div class="step" style="left:474px">
    <div class="step-icon"><svg width="44" height="44" viewBox="0 0 44 44" fill="none" stroke="#f25c19" stroke-width="1.6"><path d="M8 28a14 14 0 0 1 28 0z"/><line x1="5" y1="31" x2="39" y2="31"/><circle cx="22" cy="11" r="2"/></svg></div>
    <h3>Await delivery</h3>
    <p>We deliver twice weekly, on Sundays and Wednesdays<br>Our delivery window is between 3 pm and 8 pm</p>
  </div>
  <div class="step" style="left:749px">
    <div class="step-icon"><svg width="44" height="44" viewBox="0 0 44 44" fill="none" stroke="#f25c19" stroke-width="1.6"><circle cx="22" cy="22" r="13"/><circle cx="22" cy="22" r="8"/><line x1="5" y1="10" x2="5" y2="34"/><line x1="39" y1="10" x2="39" y2="34"/></svg></div>
    <h3>Heat and eat!</h3>
    <p>Place your meal in the microwave for 2-2:30 minutes or reheat to preferred temperature on a pan/skillet</p>
  </div>
  <a class="btn btn-outline">Get Started</a>
</section>

<section class="shop">
  <div class="kicker">Shop now!</div>
  <h2>Peak nutrition. Peak performance.</h2>
  <div class="cat" style="left:199px;top:134px"><div class="shot" role="img" aria-label="Premium entree dish" style="background:radial-gradient(circle,#a65a2c,#e9e2d2 70%)"></div><span>Premium Entrees</span></div>
  <div class="cat on" style="left:405px;top:134px"><div class="shot" role="img" aria-label="Entree bowl with rice" style="background:radial-gradient(circle,#d9822e,#efe9dc 70%)"></div><span>Entrees</span></div>
  <div class="cat" style="left:611px;top:134px"><div class="shot" role="img" aria-label="Breakfast pancakes with berries" style="background:radial-gradient(circle,#e3b06b,#f0e9e0 70%)"></div><span>Breakfast</span></div>
  <div class="cat" style="left:817px;top:134px"><div class="shot" role="img" aria-label="Green salad bowl" style="background:radial-gradient(circle,#5b7d35,#2f3b2a 70%)"></div><span>Salads</span></div>
  <div class="cat" style="left:302px;top:332px"><div class="shot" role="img" aria-label="Meal plate with salmon and vegetables" style="background:radial-gradient(circle,#b8643a,#e9e4d8 70%)"></div><span>Cold Pressed Juices</span></div>
  <div class="cat" style="left:508px;top:332px"><div class="shot" role="img" aria-label="Packaged snack containers" style="background:radial-gradient(circle,#cfc3b2,#f2efe9 70%)"></div><span>Snacks</span></div>
  <div class="cat" style="left:714px;top:332px"><div class="shot" role="img" aria-label="Set of pre-set plan meals" style="background:radial-gradient(circle,#c98a44,#f1ece3 70%)"></div><span>Pre-Set Plans</span></div>
  <a class="btn btn-solid">Shop Now!</a>
</section>

<section class="who">
  <h2 class="section-title">Who is <span class="accent">GFM</span> for ?</h2>
  <div class="persona" style="left:205px"><div class="shot" role="img" aria-label="Business professional at the office" style="background:linear-gradient(135deg,#c9ccd1,#6d7480)"></div><h3>Professional</h3><p>GFM is the ideal service for the professional on the go. We deliver twice weekly so you can focus on your career and prioritize your business without compromising on nutrition.</p></div>
  <div class="persona" style="left:479px"><div class="shot" role="img" aria-label="Family relaxing together on a sofa" style="background:linear-gradient(135deg,#d8cbb8,#8e7a63)"></div><h3>Families</h3><p>Set your family up for success with a week of healthy meals planned ahead. By ordering the week before, you'll be able to able to serve your family healthy meals with minimal effort!</p></div>
  <div class="persona" style="left:755px"><div class="shot" role="img" aria-label="Person relaxing with a laptop at home" style="background:linear-gradient(135deg,#d6dde3,#7f8c96)"></div><h3>Singles</h3><p>Cooking can be tiring and costly for individuals. Enjoy a clean fridge full of as many or as few meals as you need! No more wasted ingredients, just pure sustainable joy of eating!</p></div>
  <a class="btn btn-outline">Get Started</a>
</section>

<section class="team">
  <h2>Meet our team<br>of experts</h2>
  <a class="btn btn-light">Contact Us</a>
  <div class="member" style="left:405px"><div class="shot" role="img" aria-label="Portrait of the founder" style="background:linear-gradient(160deg,#8d8d8d,#3a3a3a)"></div><h3>Marco Delvane</h3><p>Founder</p></div>
  <div class="member" style="left:611px"><div class="shot" role="img" aria-label="Portrait of the CEO" style="background:linear-gradient(160deg,#a4a4a4,#4a4a4a)"></div><h3>Owen Pritchard</h3><p>CEO</p></div>
  <div class="member" style="left:817px"><div class="shot" role="img" aria-label="Meal bowl representing the operations manager" style="background:radial-gradient(circle,#d48a3a 20%,#3d8fd0 55%,#8a8a8a 75%)"></div><h3>Elena Ruiz</h3><p>Operations Manager</p></div>
</section>

<section class="bag">
  <h2 class="section-title">What's in your <span class="accent">GFM</span> bag ?</h2>
  <div class="feature" style="left:199px">
    <div class="ficon"><svg width="30" height="30" viewBox="0 0 30 30" fill="none" stroke="#f25c19" stroke-width="1.6"><path d="M9 4v8a3 3 0 0 0 3 3v11M6 4v7M12 4v7"/><path d="M21 4c-3 2-3 9 0 11v11"/></svg></div>
    <h3>Delicious Chef-In-<br>spired Meals</h3>
    <p>Our meals are designed and prepared by a team of experienced chefs with decades of experience and a passion for preparing food that is healthy, macro-nutrient friendly, yet doesn't compromise on flavor.</p>
  </div>
  <div class="feature" style="left:405px">
    <div class="ficon"><svg width="30" height="30" viewBox="0 0 30 30" fill="none" stroke="#f25c19" stroke-width="1.6"><path d="M15 4l9 4v7c0 6-4 9-9 11-5-2-9-5-9-11V8z"/></svg></div>
    <h3>Perfectly portioned<br>amounts</h3>
    <p>Each product is comprised of portioned ingredients to guarantee the nutrient content of each product, to help you more accurately gauge your daily nutritional intake.</p>
  </div>
  <div class="feature" style="left:611px">
    <div class="ficon"><svg width="30" height="30" viewBox="0 0 30 30" fill="none" stroke="#f25c19" stroke-width="1.6"><path d="M8 24C8 12 14 6 24 6c0 10-6 16-16 16z"/><line x1="6" y1="26" x2="16" y2="15"/></svg></div>
    <h3>Responsibly sourced-<br>quality ingredients</h3>
    <p>Our fresh produce, sustainable seafood, exclusive spice blends, and other ingredients have been meticulously curated by our team to provide the absolute best for our members.</p>
  </div>
  <div class="feature" style="left:817px">
    <div class="ficon"><svg width="30" height="30" viewBox="0 0 30 30" fill="none" stroke="#f25c19" stroke-width="1.6"><path d="M12 7l3-4 3 4M20 10l4 7-3 4M10 10l-4 7 3 4M10 24h10"/></svg></div>
    <h3>Recyclable ice packs<br>and packaging</h3>
    <p>Our meals and other products are delivered fresh in our specially made reusable insulated bags. Each bag is packed with an icepack to maintain freshness! Our in-house team of delivery drivers conveniently pick up our bags and packs during deliveries and return them to our facility to be sanitized and reused for future deliveries.</p>
  </div>
  <a class="btn btn-solid">Choose Your Plan</a>
</section>

<section class="gift">
  <svg class="abs" style="left:0;top:0" width="1200" height="313" viewBox="0 0 1200 313"><polygon points="660,0 1200,0 1200,313 525,313" fill="#f25c19"/></svg>
  <h2>Easy gift giving</h2>
  <p>The gift that lets them choose! Easy, personalized, convenient, gift giving. Plus no transaction fees or card expiry dates? That's a lot of reasons our Gift Cards make great gifts!</p>
  <a class="btn btn-solid">Choose Your Plan</a>
  <div class="gift-photo" role="img" aria-label="Insulated meal delivery bag on a kitchen counter"></div>
</section>

<section class="reviews">
  <h2 class="section-title">Happy clients say</h2>
  <div class="quote-badge"><div>“</div></div>
  <svg class="arrow" style="left:198px" width="14" height="24" viewBox="0 0 14 24"><path d="M12 2L2 12l10 10" fill="none" stroke="#555" stroke-width="1.5"/></svg>
  <svg class="arrow" style="left:988px" width="14" height="24" viewBox="0 0 14 24"><path d="M2 2l10 10L2 22" fill="none" stroke="#555" stroke-width="1.5"/></svg>
  <blockquote>"This meal service has been an absolute life saver!! They offer super healthy meals and we are really enjoying the low-carb option with lots of vegetables. This service is a huge time saver for our busy lifestyle and it will definitely assist with our weight loss goals. We also love that there is minimal waste. We have thoroughly enjoyed every meal that we have tried so far and we are satisfied with the portions. We will definitely be long-term customers.<br><b>Thanks GFM!!"</b></blockquote>
  <div class="by">-- Nadia --</div>
  <div class="dots"><i></i><i class="on"></i><i></i><i></i></div>
</section>

<section class="join">
  <div class="join-photo" role="img" aria-label="Meal container with grilled chicken, rice and fresh vegetables"></div>
  <h2>Join the <span class="accent">GFM</span> family!</h2>
  <p>Become a member and earn points &amp; exclusive rewards every time you order or <b>refer a friend!</b></p>
  <a class="btn btn-solid b1">Join Now!</a>
  <a class="btn btn-outline b2">Join Now!</a>
</section>

<footer class="site-footer">
  <div class="footer-brand">Go Fuel Meals</div>
  <div class="fcol" style="left:344px">
    <h4>Quick Links</h4>
    <ul><li>Meal Menu</li><li>About Us</li><li>Term Of Service</li><li>Refund Policy</li><li>Blog</li><li>Shipping Policy</li><li>Privacy Policy</li></ul>
  </div>
  <div class="fcol" style="left:533px">
    <h4>We're Here to Help!</h4>
    <div class="row"><svg width="11" height="11" viewBox="0 0 12 12"><path d="M2 1l2.5 0 1 3-1.5 1a7 7 0 0 0 3 3l1-1.5 3 1V11C5 11 1 7 1 2z" fill="none" stroke="#f25c19" stroke-width="1.2"/></svg>(416) 555 0142</div>
    <div class="row"><svg width="11" height="9" viewBox="0 0 12 9"><rect x="0.5" y="0.5" width="11" height="8" fill="none" stroke="#f25c19"/><path d="M0.5 0.5L6 5l5.5-4.5" fill="none" stroke="#f25c19"/></svg>hello@gofuelmeals.com</div>
    <div class="row" style="margin-top:4px">Get Connected</div>
    <div class="socials"><i></i><i class="on"></i><i></i><i></i></div>
  </div>
  <div class="fcol newsletter" style="left:762px">
    <h4>Want to Keep in Touch?</h4>
    <p>Newsletter Promo Sign Up Receive 10% Off First Purchase...</p>
    <div class="field">Enter Your Email...</div>
    <a class="btn btn-solid">Submit</a>
  </div>
  <div class="footer-rule"></div>
  <div class="cities">
    <h5>Best prepared meal delivery in Canada!</h5>
    <p>Ajax &nbsp;|&nbsp; Ancaster &nbsp;|&nbsp; Aurora &nbsp;|&nbsp; Bowmanville &nbsp;|&nbsp; Brampton &nbsp;|&nbsp; Burlington &nbsp;|&nbsp; Caledon &nbsp;|&nbsp; Courtice &nbsp;|&nbsp; Dundas &nbsp;|&nbsp; East Gwillimbury<br>East York &nbsp;|&nbsp; Etobicoke &nbsp;|&nbsp; Georgetown &nbsp;|&nbsp; Gormley &nbsp;|&nbsp; Guelph &nbsp;|&nbsp; Holland Landing &nbsp;|&nbsp; King City &nbsp;|&nbsp; Kleinburg &nbsp;|&nbsp; Milton<br>Mississauga &nbsp;|&nbsp; Newmarket &nbsp;|&nbsp; North York &nbsp;|&nbsp; Oakville &nbsp;|&nbsp; Pickering &nbsp;|&nbsp; Richmond Hill &nbsp;|&nbsp; Scarborough &nbsp;|&nbsp; Stouffville &nbsp;|&nbsp; Thornhill<br>Toronto &nbsp;|&nbsp; Vaughan &nbsp;|&nbsp; Waterdown &nbsp;|&nbsp; Whitby &nbsp;|&nbsp; Woodbridge &nbsp;|&nbsp; York</p>
  </div>
  <div class="copy">© 2022 <b>GFM Meals.</b> All Rights Reserved.</div>
  <svg class="abs" style="left:1092px;top:422px" width="16" height="16" viewBox="0 0 16 16"><polygon points="8,1 15,15 8,11 1,15" fill="#f25c19"/></svg>
</footer>

</body>
</html>
```